business card design.

2 sided transparent design like my current card with the attached logo. Super simple, should take someone 5-10 minutes tops. Cell number will be embossed. You could put the web URL on the back of the logo with white blocker background as www.vex-kl.com. The chip is foil to make it look like a credit card. Any suggested ways to improve the design are welcome. The mag stripe should be printed on the back of the card. Instead of Brimly the company name will be Vex

```html
<!DOCTYPE html>
<html lang="en">
<head>
<meta charset="utf-8">
<title>Vex business card, front and back</title>
<link rel="stylesheet" href="https://fonts.googleapis.com/css2?family=Arimo:wght@400;700&display=swap">
<style>
  :root {
    --canvas: #ece8e6;
    --card-edge: #c9c2c0;
    --tint-rose: #e2a6a6;
    --tint-blush: #efdcd9;
    --tint-cream: #f0e6bf;
    --tint-mist: #d6e3e2;
    --band-grey: rgba(120, 112, 112, 0.35);
    --emboss-band: rgba(105, 100, 102, 0.82);
    --ink: #111111;
    --silver-light: #f4f4f4;
    --silver-dark: #9c9c9c;
    --stripe: #231f20;
    --white: #ffffff;
    --chip-gold: #f2d54a;
    --chip-line: #6b5a12;
    --mark-dot: #e36a5c;
  }
  * { margin: 0; padding: 0; box-sizing: border-box; }
  html, body { width: 1200px; height: 913px; overflow: hidden; }
  body {
    background: var(--canvas);
    font-family: "Arimo", Arial, sans-serif;
    position: relative;
  }
  .card {
    position: absolute;
    width: 520px;
    height: 320px;
    border-radius: 18px;
    overflow: hidden;
    border: 1px solid var(--card-edge);
    box-shadow: 0 8px 24px rgba(0,0,0,0.12);
  }
  .card--front { left: 560px; top: 100px; }
  .card--back  { left: 120px; top: 490px; }

  .card__backdrop {
    position: absolute; inset: 0;
    background:
      radial-gradient(circle at 25% 75%, var(--tint-rose) 0%, transparent 45%),
      radial-gradient(circle at 45% 20%, var(--tint-rose) 0%, transparent 30%),
      radial-gradient(circle at 80% 60%, var(--tint-cream) 0%, transparent 40%),
      radial-gradient(circle at 75% 85%, var(--tint-mist) 0%, transparent 30%),
      var(--tint-blush);
  }
  .card--back .card__backdrop { transform: scaleX(-1); }

  .card__band {
    position: absolute; left: 0; right: 0; top: 76px; height: 38px;
    background: var(--band-grey);
  }

  .chip { position: absolute; left: 30px; top: 64px; width: 58px; height: 60px; }

  .brand {
    position: absolute; left: 372px; top: 72px;
    display: flex; align-items: center; gap: 10px;
  }
  .brand__dot { width: 22px; height: 22px; border-radius: 50%; background: var(--mark-dot); }
  .brand__name { font-size: 38px; font-weight: 700; color: #333; line-height: 1; }

  .contact {
    position: absolute; top: 228px; left: 30px; right: 20px;
    display: flex; justify-content: space-between;
    font-size: 19px; font-weight: 700; color: var(--ink);
  }

  .emboss-band {
    position: absolute; left: 0; right: 0; bottom: 0; height: 54px;
    background: var(--emboss-band);
    display: flex; align-items: center; justify-content: center;
  }
  .emboss-band__number {
    font-size: 31px; font-weight: 700; letter-spacing: 1px;
    color: var(--silver-light);
    text-shadow: 0 -1px 0 var(--silver-dark), 0 2px 1px rgba(0,0,0,0.45);
  }

  .mag-stripe {
    position: absolute; left: 0; right: 0; top: 76px; height: 38px;
    background: var(--stripe);
    display: flex; align-items: center; justify-content: center;
  }
  .mag-stripe__url { color: var(--white); font-size: 18px; font-weight: 700; }

  .show-through { position: absolute; inset: 0; transform: scaleX(-1); opacity: 0.35; }
  .show-through .contact { color: #6a6a6a; font-weight: 400; }
  .show-through .emboss-band { background: rgba(105,100,102,0.55); }
  .show-through .emboss-band__number { color: #d8d8d8; }
</style>
</head>
<body>

<section class="card card--front" aria-label="Card front">
  <div class="card__backdrop" role="img" aria-label="Soft overlapping rose, cream and mist colour shapes on clear frosted plastic"></div>
  <div class="card__band"></div>
  <svg class="chip" viewBox="0 0 58 60" aria-label="Foil chip">
    <rect x="1" y="1" width="56" height="58" rx="10" fill="var(--chip-gold)" stroke="var(--chip-line)" stroke-width="1.5"/>
    <path d="M1 20H17M1 40H17M41 20H57M41 40H57M29 1V12M29 48V59" stroke="var(--chip-line)" stroke-width="1.2" fill="none"/>
    <rect x="17" y="12" width="24" height="36" rx="6" fill="none" stroke="var(--chip-line)" stroke-width="1.2"/>
  </svg>
  <div class="brand">
    <span class="brand__dot"></span>
    <span class="brand__name">Vex</span>
  </div>
  <div class="contact">
    <span class="contact__name">Marcus Hale</span>
    <span class="contact__email">Email: hello@vexmail.com</span>
  </div>
  <div class="emboss-band">
    <span class="emboss-band__number">CELL: 055-246 813 579</span>
  </div>
</section>

<section class="card card--back" aria-label="Card back">
  <div class="card__backdrop" role="img" aria-label="Soft overlapping rose, cream and mist colour shapes on clear frosted plastic"></div>
  <div class="show-through" aria-hidden="true">
    <div class="contact">
      <span>Marcus Hale</span>
      <span>Email: hello@vexmail.com</span>
    </div>
    <div class="emboss-band">
      <span class="emboss-band__number">CELL: 055-246 813 579</span>
    </div>
  </div>
  <div class="mag-stripe">
    <span class="mag-stripe__url">www.vex-kl.com</span>
  </div>
</section>

</body>
</html>
```